Webdesign für einen Softwarehersteller
Zielgruppe
Wir sind Softwarehersteller einer Arbeitsschutz Management Software. Unser Leistungsumfang beträgt
a) die Analyse, Beurteilung und Risikoeinschätzung von Gefährdungen an einem Arbeitsplatz, einer Maschine oder Tätigkeit
b) die Unterweisung von Mitarbeitern
c) ein Risiko- und Maßnahmenmanagement
d) ein Unfallmanagement bei welchem Unfälle erfasst, ausgewertet und präventive Maßnahmen ergriffen werden
e) ein Management zur Verwaltung von Gefahrstoffen inkl. der Ableitung von präventiven Maßnahmen
f) ein Tool zur Auditierung von Prozessen, wie z.B. ISO-Normen
Unsere Zielgruppe sind Industrieunternehmen ab 500 Mitarbeitern. Der Traumkunde hat 4000 - 8000 Mitarbeiter. Unsere Software ist multilingual und kann auch weltweit eingesetzt werden womit auch weltweit operierende Konzerne zu unserer Zielgruppe gehören.
Mit unserer Software dokumentiert das Unternehmen alle notwendigen Prozesse zur Einhaltung des Arbeitsschutzes. Die Software unterstützt dabei das Unternehmen, die Menschen im Unternehmen best möglich zu schützen und allen rechtlichen Anforderungen gerecht zu werden.
Aufgabenstellung
Hallo Designer:innen,
zuerst möchte ich mich bei euch bedanken, dass Ihr euch an unserem Projekt beteiligt. Wir suchen eine Homepage, sehr clean, sehr modern und passend zu einem Softwareprodukt z.B. https://brennlaub.com/seiten-vorlagen (Kalvorix Theme). Wir legen Wert auf Struktur, Übersichtlichkeit, Modern.
Textinhalte findet Ihr auf der bestehenden Homepage.
WICHTIG!!!
a) Die bestehende Homepage dient als Inhaltsvorlage. Wir finden die Homepage nicht gut!
b) Wir erwarten, ein Hochwertiges Design sowie eine durchdachte Aufteilung der Homepage. Wenn Ihr z.B. der Meinung seid, dass auf der Landingpage eine Produktgallerie mit Bildern notwendig ist, dann fügt diese bitte ein und verwendet Demo-Bilder. Wir liefern gerne später Inhalte für die Bereiche. Die neue Webseite darf gerne von der bestehenden Struktur abweichen.
c) Selvadon wird ein neues, moderneres Logo erhalten. Das neue Logo findet Ihr unter
https://stage.selvadon.de/wp-content/uploads/2022/02/test_logo1.png
https://stage478.selvadon.de/wp-content/uploads/2022/03/Logo_web.png

```html
<!DOCTYPE html>
<html lang="de">
<head>
<meta charset="utf-8">
<title>Selvadon – Software für Arbeitsschutz</title>
<link href="https://fonts.googleapis.com/css2?family=Lato:wght@400;700;900&display=swap" rel="stylesheet">
<style>
  :root {
    --hero-green: #cfe0c6;
    --hero-circle: #c0d6b4;
    --accent: #5dbb45;
    --accent-dark: #3f8f2e;
    --ink: #2e2e2e;
    --ink-soft: #4a4a4a;
    --paper: #ffffff;
    --photo: #b9c2c6;
    --device: #d9dcdd;
  }
  * { margin: 0; padding: 0; box-sizing: border-box; }
  html, body { width: 1200px; height: 800px; overflow: hidden; background: var(--paper); }
  body { font-family: "Lato", sans-serif; color: var(--ink); position: relative; }

  .hero-bg { position: absolute; inset: 0; }

  .brand { position: absolute; left: 64px; top: 48px; display: flex; align-items: center; gap: 10px; }
  .brand-mark { width: 22px; height: 22px; background: var(--accent-dark); }
  .brand-name { font-size: 15px; font-weight: 700; letter-spacing: 4px; color: var(--ink-soft); }

  .main-nav { position: absolute; left: 300px; top: 76px; display: flex; gap: 64px; }
  .nav-link { font-size: 12px; font-weight: 700; letter-spacing: .4px; color: var(--ink); text-decoration: none; position: relative; }
  .nav-link.is-active::after { content: ""; position: absolute; left: 0; right: 0; bottom: -9px; height: 4px; background: var(--accent); }

  .contact-person { position: absolute; left: 860px; top: 40px; display: flex; gap: 22px; }
  .contact-photo { width: 90px; height: 90px; border-radius: 50%; background: radial-gradient(circle at 50% 40%, #d6dadc, var(--photo)); border: 4px solid #e9eee6; }
  .contact-info { text-align: right; padding-top: 14px; }
  .contact-name { font-size: 14px; font-weight: 700; color: var(--ink); }
  .contact-role { font-size: 13px; color: var(--ink-soft); margin-top: 2px; }
  .btn { display: inline-block; background: var(--accent); color: var(--paper); font-weight: 700; font-size: 12px; letter-spacing: .4px; text-decoration: none; }
  .btn-appointment { margin-top: 14px; padding: 8px 18px; }

  .hero-copy { position: absolute; left: 170px; top: 200px; width: 480px; }
  .hero-title { font-size: 66px; font-weight: 900; line-height: 1.08; color: var(--ink); }
  .hero-lead { font-size: 23px; line-height: 1.35; color: var(--ink); margin-top: 22px; }
  .hero-actions { margin-top: 40px; display: flex; align-items: center; gap: 34px; }
  .btn-primary { padding: 18px 22px; font-size: 13px; }
  .link-more { font-size: 13px; font-weight: 700; color: var(--ink); text-decoration: none; display: flex; align-items: center; gap: 8px; }

  .product-visual { position: absolute; left: 700px; top: 290px; width: 360px; height: 400px; }
</style>
</head>
<body>
  <svg class="hero-bg" width="1200" height="800" viewBox="0 0 1200 800" aria-hidden="true">
    <defs>
      <clipPath id="heroClip">
        <path d="M0 0 H1200 V360 C1020 500 760 650 400 650 C240 650 90 625 0 600 Z"/>
      </clipPath>
    </defs>
    <g clip-path="url(#heroClip)">
      <rect width="1200" height="800" fill="var(--hero-green)"/>
      <circle cx="520" cy="290" r="380" fill="var(--hero-circle)"/>
    </g>
  </svg>

  <header>
    <div class="brand">
      <span class="brand-mark"></span>
      <span class="brand-name">SELVADON</span>
    </div>
    <nav class="main-nav">
      <a class="nav-link is-active" href="#">HOME</a>
      <a class="nav-link" href="#">SOFTWARE MODULE</a>
      <a class="nav-link" href="#">UNTERNEHMEN</a>
      <a class="nav-link" href="#">KONTAKT</a>
    </nav>
    <div class="contact-person">
      <div class="contact-photo" role="img" aria-label="Porträtfoto des Ansprechpartners"></div>
      <div class="contact-info">
        <div class="contact-name">Jonas Weller</div>
        <div class="contact-role">Ihr persönlicher Ansprechpartner</div>
        <a class="btn btn-appointment" href="#">TERMIN VEREINBAREN</a>
      </div>
    </div>
  </header>

  <main>
    <section class="hero-copy">
      <h1 class="hero-title">Software für Arbeitschutz</h1>
      <p class="hero-lead">mit einer breiten Palette an Modulen und Funktionen</p>
      <div class="hero-actions">
        <a class="btn btn-primary" href="#">ENTDECKEN</a>
        <a class="link-more" href="#">WARUM SELVADON
          <svg width="9" height="10" viewBox="0 0 9 10" aria-hidden="true"><path d="M0 0 L9 5 L0 10 Z" fill="var(--ink)"/></svg>
        </a>
      </div>
    </section>

    <div class="product-visual" role="img" aria-label="Bildschirm mit Ansicht der Arbeitsschutz-Software"
         style="background: linear-gradient(160deg, #e6e9ea 0%, var(--device) 60%, #c9cdce 100%); border-radius: 8px;"></div>
  </main>
</body>
</html>
```